BHSC Business cards

We are an established dental practice that is looking for new business cards to match our new logo. We are looking for something unique and sophisticated.
BRIEF: Colours are black, silver and white. Include the company name, logo (including “Pelwick Heath Dental Care”) and phone number “03 9415 2876”.
Front - Include the company name, logo (including “Pelwick Heath Dental Care”) and phone number “03 9415 2876”.
Back - Include the company name,  “Pelwick Heath Dental Care”, phone number “03 9415 2876”. address "64A Tindle Street, Pelwick Heath, Vic 3187", "Email reception@pelwickheathdentalcare.com.au", the Dentist Name " Dr ................................"  Your next appointment "Day, date and time(am/pm)".  3 lines for 3 appointments please, and at the bottom "IF UNABLE TO KEEP THIS APPOINTMENT 48 HOURS NOTICE IS REQUIRED."
Try and be creative and different with the design, i've added an image for inspiration

Target Market(s)
ALL in need of dental
Industry/Entity Type
Dental Clinic
Look and feel
Each slider illustrates characteristics of the customer's brand and the style your logo design should communicate.

```html
<!DOCTYPE html>
<html lang="en">
<head>
<meta charset="utf-8">
<title>Pelwick Heath Dental Care – Business Cards</title>
<link rel="stylesheet" href="https://fonts.googleapis.com/css2?family=Poppins:wght@300;400;500;600&display=swap">
<style>
  :root {
    --backdrop: #858585;
    --card-white: #ffffff;
    --card-black: #231f20;
    --card-black-light: #2e2a2b;
    --ink: #1f1b1c;
    --ink-soft: #3a3637;
    --paper: #ffffff;
  }
  * { box-sizing: border-box; margin: 0; padding: 0; }
  html, body { width: 1200px; height: 1200px; overflow: hidden; }
  body {
    background: var(--backdrop);
    font-family: "Poppins", sans-serif;
    color: var(--ink);
    position: relative;
  }
  .card {
    position: absolute;
    left: 262px;
    width: 686px;
    border-radius: 19px;
    overflow: hidden;
  }
  .card--front { top: 165px; height: 381px; background: var(--card-white); }
  .card--back {
    top: 653px; height: 391px;
    background: radial-gradient(circle at 50% 40%, var(--card-black-light), var(--card-black) 70%);
  }

  /* front header */
  .mark-circle { position: absolute; left: 107px; top: 37px; width: 106px; height: 106px; border-radius: 50%; background: var(--ink); }
  .divider { position: absolute; left: 244px; top: 37px; width: 1.5px; height: 102px; background: var(--ink); }
  .brand { position: absolute; left: 270px; top: 30px; }
  .brand__name { font-weight: 600; font-size: 30px; line-height: 36px; letter-spacing: 0.5px; color: var(--ink); text-transform: uppercase; }
  .brand__sub { font-weight: 600; font-size: 15.5px; letter-spacing: 2.6px; line-height: 20px; color: var(--ink); text-transform: uppercase; }
  .contact { position: absolute; left: 270px; top: 92px; font-size: 14px; line-height: 17px; color: var(--ink); }
  .contact li { list-style: none; display: flex; align-items: center; gap: 7px; }
  .contact svg { width: 10px; height: 10px; flex: none; fill: var(--ink); }

  /* appointment form */
  .form { position: absolute; left: 66px; right: 60px; top: 172px; font-size: 15px; }
  .row { display: flex; align-items: baseline; height: 41px; white-space: nowrap; }
  .row .label { font-weight: 600; }
  .row .dots { flex: 1; border-bottom: 1.5px dotted var(--ink-soft); margin: 0 5px; transform: translateY(-3px); }
  .row .dots--day { flex: 0 0 170px; }
  .row .dots--date { flex: 0 0 150px; }
  .row .dots--time { flex: 0 0 80px; }
  .row .at { margin-left: 3px; font-weight: 400; }
  .row .ampm { font-size: 13px; font-weight: 400; }
  .row .next { font-weight: 400; font-size: 15.5px; }
  .notice { position: absolute; left: 66px; top: 432px; }
  .card--front .notice { top: 344px; font-size: 12.5px; letter-spacing: 2.3px; text-transform: uppercase; }

  /* back */
  .back-mark { position: absolute; left: 112px; top: 152px; width: 78px; height: 78px; border-radius: 50%; background: var(--paper); }
  .back-brand { position: absolute; left: 209px; top: 160px; color: var(--paper); }
  .back-brand .brand__name { color: var(--paper); font-size: 34px; line-height: 40px; }
  .back-brand .brand__sub { color: var(--paper); font-size: 18px; letter-spacing: 3px; line-height: 24px; }
</style>
</head>
<body>

<section class="card card--front" aria-label="Appointment card">
  <div class="mark-circle" aria-hidden="true"></div>
  <div class="divider" aria-hidden="true"></div>
  <div class="brand">
    <p class="brand__name">Pelwick Heath</p>
    <p class="brand__sub">Dental Care — 03 9415 2876</p>
  </div>
  <ul class="contact">
    <li><svg viewBox="0 0 10 10"><path d="M5 0a3.6 3.6 0 0 0-3.6 3.6C1.4 6.3 5 10 5 10s3.6-3.7 3.6-6.4A3.6 3.6 0 0 0 5 0zm0 5a1.4 1.4 0 1 1 0-2.8A1.4 1.4 0 0 1 5 5z"/></svg>64A Tindle Street, Pelwick Heath, Vic 3187</li>
    <li><svg viewBox="0 0 10 10"><path d="M0 2h10v1L5 6 0 3zm0 2l5 3 5-3v4H0z"/></svg>reception@pelwickheathdentalcare.com.au</li>
    <li><svg viewBox="0 0 10 10"><circle cx="5" cy="5" r="5"/></svg>www.pelwickheathdentalcare.com.au</li>
  </ul>

  <div class="form">
    <div class="row"><span class="label">DR</span><span class="dots"></span><span class="next">Your next appointment</span></div>
    <div class="row"><span class="label">Day</span><span class="dots dots--day"></span><span class="label">Date</span><span class="dots dots--date"></span><span class="at">at</span><span class="dots dots--time"></span><span class="ampm">AM/PM</span></div>
    <div class="row"><span class="label">Day</span><span class="dots dots--day"></span><span class="label">Date</span><span class="dots dots--date"></span><span class="at">at</span><span class="dots dots--time"></span><span class="ampm">AM/PM</span></div>
    <div class="row"><span class="label">Day</span><span class="dots dots--day"></span><span class="label">Date</span><span class="dots dots--date"></span><span class="at">at</span><span class="dots dots--time"></span><span class="ampm">AM/PM</span></div>
  </div>
  <p class="notice">If unable to keep this appointment 48 hours notice is required.</p>
</section>

<section class="card card--back" aria-label="Brand card">
  <div class="back-mark" aria-hidden="true"></div>
  <div class="back-brand">
    <p class="brand__name">Pelwick Heath</p>
    <p class="brand__sub">Dental Care — 03 9415 2876</p>
  </div>
</section>

</body>
</html>
```